Business card for a doctor's practice

Would like a business card for a Pulmonary ( lung) doctor. I would like to include a logo with something in reference to air or oxygen or lungs. Would like the color red included somehow. Name of the company is Breathwell Medical Associates of Eastern Carolina and we specialize in Pulmonary Medicine,. I would like something streamlined and modern
Target Market(s)
Patients, hospitals, other doctors
Industry/Entity Type
Business
Contact Information for Business Card
Would like business details superimposed on a logo somehow
Look and feel

```html
<!DOCTYPE html>
<html lang="en">
<head>
<meta charset="utf-8">
<title>Breathwell Medical Associates – Business Card</title>
<link rel="stylesheet" href="https://fonts.googleapis.com/css2?family=Tinos:wght@400;700&display=swap">
<style>
  :root {
    --backdrop: #e9e5df;
    --card-white: #ffffff;
    --card-black: #0b0b0b;
    --card-black-glow: #3a3a3a;
    --ink: #111111;
    --accent-red: #e0261f;
    --rule: #222222;
    --paper-edge: #d8d8d8;
  }
  * { margin: 0; padding: 0; box-sizing: border-box; }
  html, body {
    width: 1200px;
    height: 900px;
    overflow: hidden;
    background: var(--backdrop);
    font-family: "Tinos", "Times New Roman", serif;
    color: var(--ink);
  }
  .canvas { position: relative; width: 1200px; height: 900px; }

  .card {
    position: absolute;
    width: 560px;
    height: 320px;
    border-radius: 3px;
    box-shadow: 0 10px 24px rgba(0,0,0,0.22);
  }

  /* Front */
  .card-front {
    left: 80px; top: 100px;
    background: var(--card-white);
    border: 1px solid var(--paper-edge);
  }
  .front-brand {
    position: absolute;
    left: 34px; top: 108px;
    width: 230px;
    display: flex;
    align-items: center;
    gap: 12px;
  }
  .brand-dot {
    flex: none;
    width: 16px; height: 16px;
    border-radius: 50%;
    background: var(--accent-red);
  }
  .brand-name {
    font-size: 17px;
    line-height: 1.2;
    font-weight: 400;
    letter-spacing: 0.5px;
    text-transform: uppercase;
    color: var(--ink);
  }
  .front-divider {
    position: absolute;
    left: 288px; top: 52px;
    width: 1px; height: 120px;
    background: var(--rule);
  }
  .contact-block {
    position: absolute;
    left: 310px; top: 50px;
  }
  .person-name {
    font-size: 22px;
    font-weight: 700;
    line-height: 1.1;
  }
  .person-title {
    font-size: 13px;
    color: var(--accent-red);
    margin-top: 3px;
  }
  .contact-line {
    display: flex;
    align-items: center;
    gap: 8px;
    font-size: 14px;
    margin-top: 7px;
  }
  .contact-line:first-of-type { margin-top: 10px; }
  .contact-icon { width: 12px; height: 12px; flex: none; }
  .address-block {
    position: absolute;
    left: 310px; top: 228px;
    font-size: 14px;
    line-height: 1.4;
  }

  /* Back */
  .card-back {
    left: 560px; top: 480px;
    background: radial-gradient(ellipse at 45% 40%, var(--card-black-glow) 0%, var(--card-black) 70%);
    display: flex;
    align-items: center;
    justify-content: center;
  }
  .back-brand {
    display: flex;
    align-items: center;
    gap: 16px;
    width: 340px;
  }
  .back-brand .brand-dot {
    width: 22px; height: 22px;
    background: var(--card-white);
  }
  .back-brand .brand-name {
    font-size: 22px;
    color: var(--card-white);
  }
</style>
</head>
<body>
<main class="canvas">

  <section class="card card-front" aria-label="Business card front">
    <div class="front-brand">
      <span class="brand-dot"></span>
      <p class="brand-name">Breathwell Medical Associates of Eastern Carolina</p>
    </div>

    <div class="front-divider"></div>

    <div class="contact-block">
      <h1 class="person-name">Lena Marsh, MD</h1>
      <p class="person-title">Consultant</p>
      <p class="contact-line">
        <svg class="contact-icon" viewBox="0 0 12 12" aria-hidden="true">
          <path d="M2.5 1 L4.5 1 L5.2 3.4 L4 4.3 Q5 6.8 7.7 8 L8.6 6.8 L11 7.5 L11 9.5 Q11 11 9.5 11 Q1 10.2 1 2.5 Q1 1 2.5 1 Z" fill="var(--accent-red)"/>
        </svg>
        (252) 555-0174
      </p>
      <p class="contact-line">
        <svg class="contact-icon" viewBox="0 0 12 12" aria-hidden="true">
          <rect x="3" y="1" width="6" height="3" fill="var(--accent-red)"/>
          <rect x="1" y="4.5" width="10" height="5" rx="1" fill="var(--accent-red)"/>
          <rect x="3" y="8" width="6" height="3" fill="var(--accent-red)" stroke="#fff" stroke-width="0.8"/>
        </svg>
        (252) 555-0188
      </p>
    </div>

    <address class="address-block" style="font-style: normal;">
      1820 Harbor Pointe Drive<br>
      Greenville, NC 27858
    </address>
  </section>

  <section class="card card-back" aria-label="Business card back">
    <div class="back-brand">
      <span class="brand-dot"></span>
      <p class="brand-name">Breathwell Medical Associates of Eastern Carolina</p>
    </div>
  </section>

</main>
</body>
</html>
```